Branvique needs a business Card Design

We are looking for a business card Design for our new Managed Service Provider Company, Branvique. Branvique encompasses everything IT for the average medium sized business. Our primary services are help desk support, cyber-security (malware and ransomware protection), and Disaster Recovery systems. We would like the design to have a very clean and professional look, with a very minimalist feel.

Target Market(s)

Medium to large sized businesses

Industry/Entity Type

It Service

Contact Information for Business Card

Name GoesHere
name@branvique.com
O: 555-382-6047
C: 555-731-5820

Font styles to use
Other font styles liked:
• Poppins Font Only Please

Colors

Designer to choose only greyscale colors for use in the design.

Requirements
Must have
• Logo included
Nice to have
• Cutting Edge, innovative, minimalistic, elegant

```html
<!DOCTYPE html>
<html lang="en">
<head>
<meta charset="UTF-8">
<title>Branvique — Business Card</title>
<link href="https://fonts.googleapis.com/css2?family=Poppins:wght@300;400;500&display=swap" rel="stylesheet">
<style>
  :root {
    --canvas-bg: #d9dadc;
    --card-charcoal: #2a2b2e;
    --card-charcoal-deep: #1c1d1f;
    --ink-light: #eeeeee;
    --ink-soft: #c6c6c6;
    --rule: #8e8e8e;
    --mark: #f2f2f2;
  }
  * { margin: 0; padding: 0; box-sizing: border-box; }
  html, body {
    width: 1200px;
    height: 900px;
    overflow: hidden;
    background: var(--canvas-bg);
    font-family: "Poppins", sans-serif;
  }
  .canvas {
    width: 1200px;
    height: 900px;
    display: flex;
    flex-direction: column;
    align-items: center;
    justify-content: center;
    gap: 60px;
  }
  .card {
    width: 560px;
    height: 320px;
    background: linear-gradient(160deg, var(--card-charcoal) 0%, var(--card-charcoal-deep) 100%);
    border-radius: 4px;
    box-shadow: 0 18px 40px rgba(0, 0, 0, 0.35);
    position: relative;
    color: var(--ink-light);
  }
  .card-front {
    display: flex;
    align-items: center;
  }
  .brand-block {
    width: 50%;
    display: flex;
    justify-content: center;
    align-items: center;
  }
  .brand-lockup {
    display: flex;
    align-items: center;
    gap: 14px;
  }
  .brand-square {
    width: 16px;
    height: 16px;
    background: var(--mark);
    flex: none;
  }
  .brand-name {
    font-weight: 300;
    font-size: 19px;
    letter-spacing: 6px;
    text-transform: uppercase;
    color: var(--ink-light);
  }
  .divider {
    width: 1px;
    height: 150px;
    background: var(--rule);
  }
  .contact-block {
    padding-left: 32px;
  }
  .person-name {
    font-weight: 500;
    font-size: 17px;
    letter-spacing: 0.5px;
    text-transform: uppercase;
    margin-bottom: 12px;
  }
  .contact-list { list-style: none; }
  .contact-item {
    display: flex;
    align-items: center;
    gap: 9px;
    font-weight: 300;
    font-size: 14px;
    line-height: 24px;
    color: var(--ink-soft);
  }
  .contact-icon {
    width: 12px;
    height: 12px;
    flex: none;
  }
  .card-back {
    display: flex;
    justify-content: center;
    align-items: center;
  }
  .card-back .brand-square {
    width: 20px;
    height: 20px;
  }
  .card-back .brand-name {
    font-size: 22px;
  }
</style>
</head>
<body>
<main class="canvas">
  <section class="card card-front" aria-label="Business card front">
    <div class="brand-block">
      <div class="brand-lockup">
        <span class="brand-square" aria-hidden="true"></span>
        <span class="brand-name">Branvique</span>
      </div>
    </div>
    <div class="divider"></div>
    <div class="contact-block">
      <p class="person-name">Marcus Hale</p>
      <ul class="contact-list">
        <li class="contact-item">
          <svg class="contact-icon" viewBox="0 0 12 12" fill="none" stroke="currentColor" stroke-width="1">
            <circle cx="6" cy="6" r="5.3"/>
            <path d="M4 3.3 L4.9 4.6 L4.3 5.2 Q5 6.8 6.8 7.7 L7.4 7.1 L8.7 8 L8 8.8 Q5.5 8.6 3.3 4.1 Z" fill="currentColor" stroke="none"/>
          </svg>
          555-382-6047
        </li>
        <li class="contact-item">
          <svg class="contact-icon" viewBox="0 0 12 12" fill="none" stroke="currentColor" stroke-width="1">
            <rect x="3.3" y="0.8" width="5.4" height="10.4" rx="1"/>
            <line x1="5.2" y1="9.4" x2="6.8" y2="9.4"/>
          </svg>
          555-731-5820
        </li>
        <li class="contact-item">
          <svg class="contact-icon" viewBox="0 0 12 12" fill="none" stroke="currentColor" stroke-width="1">
            <rect x="0.8" y="2.3" width="10.4" height="7.4"/>
            <path d="M0.8 2.3 L6 6.5 L11.2 2.3"/>
          </svg>
          name@branvique.com
        </li>
      </ul>
    </div>
  </section>

  <section class="card card-back" aria-label="Business card back">
    <div class="brand-lockup">
      <span class="brand-square" aria-hidden="true"></span>
      <span class="brand-name">Branvique</span>
    </div>
  </section>
</main>
</body>
</html>
```